Webdesign für Entwickler von onlinebasierten Terminformularen
Super Designs. Schnell und motiviert. Danke für die hervorragende Umsetzung und die Ideen!
Zielgruppe
Deutsch:
Wir sind ein Startup, das über die Seite Kalendrio.de zukünftig folgenden Service anbietet: Unternehmer können sehr flexibel (selbst) gestaltete Terminformulare erstellen und auf Ihrer Website einbinden. Kunden können dann diese Termine buchen und bekommen dann Erinnerungs-Mails und SMS.
Zielgruppe: Dienstleister wie Fotografen, Friseure, Versicherungsvertreter, Masseure, Restaurants, Arztpraxen. Also alle, die darauf angewiesen sind, dass vereinbarte Termine eingehalten werden und die die Terminvereinbarung vereinfachen wollen. Also weniger per Telefon, mehr über die eigene Website.
Englisch:
We are a start up, that is going to offer this services on the Website Kalendrio.de :
Companies can create highly flexible (self-designed) appointment forms and integrate them on their website. Customer can book appointments and will get an reminding email and SMS.
Target group: Service providers such as photographers, hairdressers, insurance agents, masseurs, restaurants, medical offices. So all those who depend on meeting agreed appointments and who want to simplify the appointment. Less by telephone, more over their own website.
Aufgabenstellung
Übersichtlichkeit, genug Weißraum, deutliche, große Überschriften, Seriös aber gerne frische Farben bei einzelnen Elementen (z.B. bei Icons oder bei Handlungsaufforderungs-Buttons), Trennlinien, Inhalte auf den Punkt.
Logo-Entwurf anbei (wird gerade hier über entwurfhafen.de ebenfalls erstellt/optimiert, siehe #817306) sagt das wesentliche aus.
Kalendrio soll also ein sehr nützliches Tool sein, das jeder schnell versteht. Daher muss auch die Website sehr übersichtlich und klar aufgebaut werden. Die wesentlichen Aussagen/Menüpunkte finden sich auf der Startseite (bzw. im Hauptmenü, siehe grober Entwurf anbei).
- frische Farben (z.B. grün, orange, gelb)
- seröse Farben/Grauwerte (z.B. blau, grau, schwarz)
- Hauptmenü/Metanavigation/Footer-Bereich
Das Design und das Teaser-Bild (Frau mit Hammer) auf dem Entwurf anbei (seite1_mit_teaser_entwurf2.jpg) sind nur als grobe Ideen (Richtung) zu verstehen. Die Startseite muss also keine Teaser-Bilder enthalten.
Der Entwurf anbei soll lediglich die ungefähre Richtung mit den angedachten Menüpunkten verdeutlichen.
Übersichtlich und modern finden wir z.B. https://talkroomly.example/de (viel Weißraum, farbige Icons, Infos übersichtlich dargeboten, lächelnde Gesichter) und übrigens auch https://www.entwurfhafen.example.
Bitte entwerfen Sie (erstmal) drei Seiten:
- Startseite
- Funktionen/Preis (Beispiel auf https://talkroomly.example/de/tools Und/oder in Tabellenform wie auf https://talkroomly.example/de/pricing/ siehe Content-Plan anbei)
- Über Kalendrio (Über uns, siehe Content-Plan anbei)
Der Content-Plan soll das Projekt verdeutlichen.
Anmerkung von unserem Programmierer: Praktisch wäre eine Basis auf Bootstrap. Dies ist aber keine Pflicht! Das Design/die Idee geht vor :-)
1zu1-Folgeaufträge (für dieses und andere Projekte im Bereich Webdesign, Flyer, CorporateDesign, Grafiken) sind sehr wahrsc..

```html
<!DOCTYPE html>
<html lang="de">
<head>
<meta charset="utf-8">
<title>Kalendrio Helpcenter</title>
<link href="https://fonts.googleapis.com/css2?family=Jost:wght@300;400;500;600&display=swap" rel="stylesheet">
<style>
:root{
  --slate:#6f7b80;
  --slate-dark:#4f5a60;
  --green:#8cc63f;
  --text:#6b757a;
  --text-soft:#8a9397;
  --line:#ececec;
  --bg-soft:#f7f7f7;
  --white:#ffffff;
}
*{box-sizing:border-box;margin:0;padding:0}
html,body{width:670px;height:1200px;overflow:hidden}
body{position:relative;font-family:'Jost',sans-serif;color:var(--text);background:var(--white)}
.abs{position:absolute}
a{color:inherit;text-decoration:none}

.meta-bar{left:0;top:0;width:670px;height:18px;background:var(--slate);color:var(--white);font-size:4.6px;font-weight:500}
.meta-bar .items{position:absolute;right:121px;top:0;height:18px;display:flex;align-items:center;gap:6px}
.meta-bar .sep{width:.5px;height:6px;background:rgba(255,255,255,.5)}

.main-nav{left:0;top:18px;width:670px;height:29px;background:var(--white);border-bottom:.5px solid var(--line)}
.brand{display:flex;align-items:center;gap:3px;font-size:12px;font-weight:500;color:var(--slate)}
.brand .dot{width:8px;height:8px;background:var(--slate);border-radius:1px}
.main-nav .brand{position:absolute;left:132px;top:7px}
.main-nav .link{position:absolute;top:10px;font-size:5.6px;color:var(--text)}
.main-nav .link.active{color:var(--slate)}
.main-nav .link.active::after{content:"";position:absolute;left:0;right:0;top:9px;height:1px;background:var(--green)}
.btn-outline{position:absolute;left:497px;top:6.5px;width:51px;height:15.5px;border:1px solid var(--green);border-radius:8px;font-size:5.6px;display:flex;align-items:center;justify-content:center;color:var(--text)}

.hero{left:0;top:47px;width:670px;height:159px;background:var(--slate);color:var(--white);text-align:center}
.hero h1{position:absolute;top:42px;left:0;right:0;font-size:15px;font-weight:500}
.hero p{position:absolute;top:65px;left:0;right:0;font-size:9.3px;font-weight:300}

.topic-card{top:162px;width:100px;height:88px;background:var(--white);box-shadow:0 2px 6px rgba(0,0,0,.07);text-align:center}
.topic-card.active{box-shadow:0 5px 12px rgba(0,0,0,.16)}
.topic-card svg{position:absolute;left:38px;top:24px;width:25px;height:25px}
.topic-card span{position:absolute;left:0;right:0;top:58px;font-size:7.4px;line-height:12px;color:var(--text)}

.section-head{left:0;width:670px;text-align:center;color:var(--slate)}
.section-head h2{font-size:14px;font-weight:500}
.section-head p{font-size:9px;font-weight:300;color:var(--text);margin-top:3px}

.faq{left:169px;width:325px;background:var(--white);box-shadow:0 1px 5px rgba(0,0,0,.1)}
.faq .q{position:absolute;left:11px;top:14px;font-size:7px;font-weight:300;color:var(--text-soft)}
.faq .toggle{position:absolute;right:11px;top:11px;width:9px;height:9px}
.faq-open{top:337px;height:112px}
.faq-open .q{top:12px;color:var(--green)}
.faq-open .toggle{top:12px}
.faq .answer{position:absolute;left:11px;right:11px;top:30px;font-size:5.4px;line-height:10.4px;color:var(--text)}
.feedback{position:absolute;left:11px;right:11px;top:66px;height:38px;background:var(--bg-soft);border-radius:3px;padding:8px 11px;font-size:6.5px;font-weight:300;color:var(--text-soft)}
.feedback .opts{margin-top:4px;font-weight:500;display:flex;gap:14px}
.faq-closed{height:31px}

.help-band{left:0;top:784px;width:670px;height:299px;background:var(--bg-soft)}
.help-card{top:889px;width:209px;height:135px;background:var(--white);box-shadow:0 1px 4px rgba(0,0,0,.08)}
.help-card h3{position:absolute;left:21px;top:22px;font-size:10px;line-height:13px;font-weight:500;color:var(--slate)}
.help-card .rule{position:absolute;left:21px;top:56px;width:27px;height:1px;background:var(--green)}
.help-card p{position:absolute;left:21px;top:63px;font-size:5.4px;line-height:8.5px;color:var(--text)}
.btn-dark{position:absolute;left:21px;top:91px;width:105px;height:23px;background:var(--slate);color:var(--white);font-size:6.6px;font-weight:500;display:flex;align-items:center;padding-left:20px}
.btn-dark::before{content:"›";position:absolute;left:7px;color:var(--green);font-size:8px}

.footer-top{left:0;top:1083px;width:670px;height:38px;background:var(--slate)}
.footer-top .brand{position:absolute;left:120px;top:11px;color:var(--white)}
.footer-top .brand .dot{background:var(--white)}
.footer-bottom{left:0;top:1121px;width:670px;height:79px;background:var(--slate-dark);color:var(--white)}
.footer-bottom .copy{position:absolute;left:120px;top:7px;font-size:5.3px}
.lang-pill{position:absolute;left:120px;top:29px;width:80px;height:17px;border:.7px solid rgba(255,255,255,.8);border-radius:9px;font-size:5.3px;display:flex;align-items:center;padding-left:11px;gap:9px}
.col{position:absolute;top:7px;font-size:5.3px}
.col h4{font-weight:500;font-size:5.3px;margin-bottom:5px}
.col li{list-style:none;line-height:9.7px;color:rgba(255,255,255,.8)}
.col .note{font-size:4.4px;line-height:7px;color:rgba(255,255,255,.75);width:100px}
.btn-green{position:absolute;left:447px;top:49px;width:101px;height:20px;background:var(--green);color:var(--white);font-size:5.8px;font-weight:500;display:flex;align-items:center;justify-content:center}
</style>
</head>
<body>

<div class="abs meta-bar">
  <div class="items"><span>Kontakt</span><span class="sep"></span><span>DE ⌵</span><span class="sep"></span><span>Zu Wertungsblick wechseln</span></div>
</div>

<nav class="abs main-nav">
  <div class="brand"><span class="dot"></span>Kalendrio</div>
  <a class="link active" style="left:210px">Funktionen / Preis</a>
  <a class="link" style="left:277px">Help-Center</a>
  <a class="link" style="left:330px">Über Uns</a>
  <a class="link" style="left:374px">Blog</a>
  <a class="link" style="left:476px">Login</a>
  <a class="btn-outline">Konto erstellen</a>
</nav>

<header class="abs hero">
  <h1>Kalendrio Helpcenter</h1>
  <p>Hier finden Sie alle Informationen und Hilfen rund um Kalendrio.</p>
</header>

<div class="abs topic-card active" style="left:120px">
  <svg viewBox="0 0 26 26" fill="none" stroke="#8cc63f" stroke-width="2"><path d="M2 6h13v11H10l-4 5v-5H2z"/><circle cx="19" cy="6" r="5" fill="#8cc63f" stroke="none"/><text x="19" y="9" font-size="8" text-anchor="middle" fill="#fff" stroke="none" font-family="sans-serif" font-weight="bold">?</text></svg>
  <span>Allgemeine Frage</span>
</div>
<div class="abs topic-card" style="left:230px">
  <svg viewBox="0 0 26 26" fill="none" stroke="#8cc63f" stroke-width="2"><path d="M2 4h18v13H13l-3 4-3-4H2z"/><path d="M5 8h9M5 11h12M5 14h10" stroke-width="1.5"/><circle cx="20" cy="6" r="5" fill="#8cc63f" stroke="none"/><text x="20" y="9" font-size="8" text-anchor="middle" fill="#fff" stroke="none" font-family="sans-serif" font-weight="bold">?</text></svg>
  <span>Technische Fragen</span>
</div>
<div class="abs topic-card" style="left:339px">
  <svg viewBox="0 0 26 26" fill="none" stroke="#8cc63f" stroke-width="2"><path d="M5 2h14v11c0 5-7 10-7 10s-7-5-7-10z"/><path d="M5 2h7v10H5z" fill="#8cc63f"/><circle cx="20" cy="19" r="5" fill="#8cc63f" stroke="none"/><text x="20" y="22" font-size="8" text-anchor="middle" fill="#fff" stroke="none" font-family="sans-serif" font-weight="bold">?</text></svg>
  <span>Fragen zur Sicherheit</span>
</div>
<div class="abs topic-card" style="left:450px">
  <svg viewBox="0 0 26 26" fill="none" stroke="#8cc63f" stroke-width="2"><rect x="2" y="5" width="20" height="17" rx="2"/><path d="M2 10h20M7 2v5M17 2v5"/><circle cx="19" cy="19" r="5" fill="#8cc63f" stroke="none"/><text x="19" y="22" font-size="8" text-anchor="middle" fill="#fff" stroke="none" font-family="sans-serif" font-weight="bold">?</text></svg>
  <span>Fragen zur<br>Terminverwaltung</span>
</div>

<div class="abs section-head" style="top:286px">
  <h2>Meist gestellte Fragen</h2>
  <p>Fragen, die oft von unseren Usern gestellt werden.</p>
</div>

<div class="abs faq faq-open">
  <div class="q">Wie nutze ich Kalendrio noch besser?</div>
  <svg class="toggle" viewBox="0 0 10 10"><path d="M0 5h10" stroke="#8cc63f" stroke-width="1.2"/></svg>
  <p class="answer">Lorem ipsum dolor sit amet, consetetur sadipscing elitr, sed diam nonumy eirmod tempor invidunt ut labore et dolore magna aliquyam erat, sed diam voluptua. At vero eos et accusam et justo duo dolores et ea rebum. Stet clita kasd gubergren, no sea takimata sanctus est Lorem ipsum dolor sit amet. Lorem ipsum dolor sit amet.</p>
  <div class="feedback">Hat Ihnen diese Antwort geholfen?<div class="opts"><span>Ja</span><span>Nein</span></div></div>
</div>

<div class="abs faq faq-closed" style="top:456px"><div class="q">Wie nutze ich Kalendrio noch besser?</div><svg class="toggle" viewBox="0 0 10 10"><path d="M0 5h10M5 0v10" stroke="#9aa1a4" stroke-width="1.2"/></svg></div>
<div class="abs faq faq-closed" style="top:494px"><div class="q">Wie nutze ich Kalendrio noch besser?</div><svg class="toggle" viewBox="0 0 10 10"><path d="M0 5h10M5 0v10" stroke="#9aa1a4" stroke-width="1.2"/></svg></div>
<div class="abs faq faq-closed" style="top:532px"><div class="q">Wie nutze ich Kalendrio noch besser?</div><svg class="toggle" viewBox="0 0 10 10"><path d="M0 5h10M5 0v10" stroke="#9aa1a4" stroke-width="1.2"/></svg></div>
<div class="abs faq faq-closed" style="top:571px"><div class="q">Wie nutze ich Kalendrio noch besser?</div><svg class="toggle" viewBox="0 0 10 10"><path d="M0 5h10M5 0v10" stroke="#9aa1a4" stroke-width="1.2"/></svg></div>
<div class="abs faq faq-closed" style="top:609px"><div class="q">Wie nutze ich Kalendrio noch besser?</div><svg class="toggle" viewBox="0 0 10 10"><path d="M0 5h10M5 0v10" stroke="#9aa1a4" stroke-width="1.2"/></svg></div>
<div class="abs faq faq-closed" style="top:647px"><div class="q">Wie nutze ich Kalendrio noch besser?</div><svg class="toggle" viewBox="0 0 10 10"><path d="M0 5h10M5 0v10" stroke="#9aa1a4" stroke-width="1.2"/></svg></div>
<div class="abs faq faq-closed" style="top:686px"><div class="q">Wie nutze ich Kalendrio noch besser?</div><svg class="toggle" viewBox="0 0 10 10"><path d="M0 5h10M5 0v10" stroke="#9aa1a4" stroke-width="1.2"/></svg></div>
<div class="abs faq faq-closed" style="top:724px"><div class="q">Wie nutze ich Kalendrio noch besser?</div><svg class="toggle" viewBox="0 0 10 10"><path d="M0 5h10M5 0v10" stroke="#9aa1a4" stroke-width="1.2"/></svg></div>

<section class="abs help-band"></section>
<div class="abs section-head" style="top:820px">
  <h2>Kalendrio Helpcenter</h2>
  <p>Hier finden Sie alle Informationen und Hilfen rund um Kalendrio.</p>
</div>

<div class="abs help-card" style="left:120px">
  <h3>Kalendrio<br>Kontaktformular</h3>
  <div class="rule"></div>
  <p>Sie haben Fragen? Dann nutzen Sie<br>gerne unser Kontaktformular</p>
  <a class="btn-dark">Zum Kontaktformular</a>
</div>
<div class="abs help-card" style="left:340px">
  <h3>Kalendrio<br>So nutzen wir Kalendrio</h3>
  <div class="rule"></div>
  <p>Sie wollen wissen, wie wir Kalendrio selbst einsetzen und<br>Tipps für Sie haben?</p>
  <a class="btn-dark" style="padding-left:17px">Zu den Kalendrio-Tipps</a>
</div>

<footer>
  <div class="abs footer-top"><div class="brand"><span class="dot"></span>Kalendrio</div></div>
  <div class="abs footer-bottom">
    <div class="copy">© 2018 Alle Rechte vorbehalten</div>
    <div class="lang-pill"><span>Sprachauswahl</span><span>DE ⌵</span></div>
    <div class="col" style="left:275px"><h4>Sonstiges</h4><ul><li>Home</li><li>Kontakt</li><li>Newsletter</li><li>Webinare</li></ul></div>
    <div class="col" style="left:320px"><h4>Benutzer</h4><ul><li>Login</li><li>Konto erstellen</li></ul></div>
    <div class="col" style="left:375px"><h4>Rechtliches</h4><ul><li>Impressum</li><li>AGB</li><li>Datenschutz</li><li>Sitemap</li></ul></div>
    <div class="col" style="left:446px"><h4>Bewertungen durch Wertungsblick.de</h4><p class="note">Verknüpfen Sie jetzt Kalendrio mit Wertungsblick.de und profitieren Sie von vertrauensvollen Usern und Transparenz.</p></div>
    <a class="btn-green">zu Wertungsblick.de wechseln</a>
  </div>
</footer>

</body>
</html>
```